" Atuamos nas áreas do direito do entretenimento, direito empresarial, direito civil. Somos uma sociedade de advogados jovens que buscam, acima de tudo, estabelecer com o cliente um vínculo de total confiança. Baseamos nosso trabalho nessa confiança mútua, transparência, comprometimento e seriedade. Nosso serviço de excelência é traduzido por nossa capacidade profissional. "

```html
<!DOCTYPE html>
<html lang="pt-BR">
<head>
<meta charset="UTF-8">
<title>Pereira, Lacerda e Soares — Papelaria</title>
<link rel="stylesheet" href="https://fonts.googleapis.com/css2?family=Cormorant+Garamond:wght@500;600&family=EB+Garamond:wght@400&display=swap">
<style>
  :root {
    --navy: #2c3f8e;
    --navy-deep: #25367a;
    --paper: #ffffff;
    --ink-soft: #8a8f9c;
    --ink-faint: #b9bdc6;
    --backdrop: #eceae6;
    --edge: #dcdad5;
    --stamp: #c9d6e3;
  }
  * { margin: 0; padding: 0; box-sizing: border-box; }
  html, body { width: 1200px; height: 1200px; overflow: hidden; }
  body {
    position: relative;
    background: var(--backdrop);
    font-family: "EB Garamond", Georgia, serif;
    color: var(--navy);
  }
  .sheet {
    position: absolute;
    background: var(--paper);
    border: 1px solid var(--edge);
  }
  .firm-name {
    font-family: "Cormorant Garamond", Georgia, serif;
    font-weight: 600;
    color: var(--navy);
    line-height: 1.1;
    white-space: nowrap;
  }
  .firm-tagline {
    font-family: "Cormorant Garamond", Georgia, serif;
    font-weight: 600;
    color: var(--navy);
    white-space: nowrap;
  }

  /* Folder */
  .folder { left: 90px; top: 70px; width: 470px; height: 640px; }
  .folder .brand { position: absolute; left: 56px; top: 150px; }
  .folder .firm-name { font-size: 33px; }
  .folder .firm-tagline { font-size: 22px; margin-top: 4px; padding-left: 70px; }

  /* Letterhead */
  .letterhead { left: 610px; top: 70px; width: 500px; height: 640px; padding: 40px 50px 0; }
  .letterhead .brand { text-align: center; }
  .letterhead .firm-name { font-size: 19px; }
  .letterhead .firm-tagline { font-size: 12px; margin-top: 2px; }
  .letter-body { margin-top: 42px; }
  .letter-body p {
    font-size: 10.5px;
    line-height: 1.55;
    color: var(--ink-soft);
    margin-bottom: 20px;
  }
  .letter-footer {
    position: absolute;
    left: 0; right: 0; bottom: 30px;
    text-align: center;
    font-size: 9px;
    color: var(--ink-soft);
    letter-spacing: 0.5px;
  }

  /* Envelope */
  .envelope { left: 90px; top: 770px; width: 620px; height: 320px; }
  .envelope .brand { position: absolute; left: 90px; top: 90px; text-align: right; }
  .envelope .firm-name { font-size: 33px; }
  .envelope .firm-tagline { font-size: 22px; margin-top: 2px; }
  .stamp-area {
    position: absolute; right: 40px; top: 34px;
    width: 58px; height: 64px;
    background: var(--stamp);
    border: 3px solid var(--paper);
    outline: 1px solid var(--edge);
  }
  .envelope-contact {
    position: absolute; left: 200px; bottom: 60px;
    font-size: 13px; color: var(--navy-deep);
  }

  /* Business cards */
  .card { width: 340px; height: 195px; }
  .card-back { left: 760px; top: 770px; background: var(--navy); border-color: var(--navy-deep); }
  .card-back .brand { position: absolute; left: 0; right: 0; top: 70px; text-align: center; }
  .card-back .firm-name { font-size: 24px; color: var(--paper); }
  .card-back .firm-tagline { font-size: 14px; color: var(--paper); margin-top: 2px; }
  .card-front { left: 760px; top: 990px; padding: 70px 30px 0 150px; }
  .card-front .person { font-size: 15px; color: var(--navy-deep); margin-bottom: 8px; }
  .card-front .detail { font-size: 10px; color: var(--ink-soft); line-height: 1.6; white-space: nowrap; }
</style>
</head>
<body>

  <section class="sheet folder" aria-label="Pasta">
    <div class="brand">
      <div class="firm-name">Pereira, Lacerda e Soares</div>
      <div class="firm-tagline">Sociedade de Advogados</div>
    </div>
  </section>

  <section class="sheet letterhead" aria-label="Papel timbrado">
    <div class="brand">
      <div class="firm-name">Pereira, Lacerda e Soares</div>
      <div class="firm-tagline">Sociedade de Advogados</div>
    </div>
    <div class="letter-body">
      <p>Nosso escritório atua com dedicação em cada caso, oferecendo orientação clara, acompanhamento próximo e soluções jurídicas ajustadas às necessidades de cada cliente.</p>
      <p>Prezamos a transparência em todas as etapas do trabalho e mantemos comunicação constante sobre o andamento de cada processo.</p>
      <p>Atendemos empresas e pessoas físicas nas áreas de entretenimento, direito empresarial e direito civil.</p>
      <p>Cada contrato é analisado com atenção aos detalhes, para prevenir conflitos e proteger os interesses envolvidos.</p>
      <p>Nossa equipe jovem alia estudo contínuo, comprometimento e seriedade no exercício da advocacia.</p>
      <p>Permanecemos à disposição para esclarecer dúvidas e agendar uma reunião em nosso escritório.</p>
    </div>
    <div class="letter-footer">Endereço · CEP · Website · Telefone</div>
  </section>

  <section class="sheet envelope" aria-label="Envelope">
    <div class="brand">
      <div class="firm-name">Pereira, Lacerda e Soares</div>
      <div class="firm-tagline">Sociedade de Advogados</div>
    </div>
    <div class="stamp-area" role="img" aria-label="Área do selo postal"></div>
    <div class="envelope-contact">Endereço · CEP · Telefone</div>
  </section>

  <section class="sheet card card-back" aria-label="Cartão de visita, verso">
    <div class="brand">
      <div class="firm-name">Pereira, Lacerda e Soares</div>
      <div class="firm-tagline">Sociedade de Advogados</div>
    </div>
  </section>

  <section class="sheet card card-front" aria-label="Cartão de visita, frente">
    <div class="person">Pereira</div>
    <div class="detail">Advogado</div>
    <div class="detail">Telefone · Celular</div>
    <div class="detail">contato@pereiralacerda.adv.br</div>
  </section>

</body>
</html>
```